KELTRIX electrical and air conditioning

the van(QMR vantoro 5 LWB in Australia) wrap design features a dynamic and eye-catching layout that enhances brand visibility while reflecting our core values and mission.
A vibrant color scheme, captures attention and evokes emotions associated with our brand. The colors are strategically placed to create a sense of movement and energy.Graphics: Bold, high-resolution graphics highlight our key services, which are refrigeration and electrical.

Target Market(s)

Locals

Requirements
Must have
• services including : Electrical/air conditioning / refrigeration / data

```html
<!DOCTYPE html>
<html lang="en">
<head>
<meta charset="utf-8">
<title>KELTRIX van wrap concepts</title>
<link rel="stylesheet" href="https://fonts.googleapis.com/css2?family=Rubik:wght@500;700;800&display=swap">
<style>
  :root {
    --page: #e9ebee;
    --wrap-white: #ffffff;
    --wrap-black: #1d1e22;
    --glass: #3a3f47;
    --tyre: #1a1a1c;
    --hub: #b9bcc1;
    --flame-orange: #f0641e;
    --flame-amber: #f7a21b;
    --flame-yellow: #f7d417;
    --ice-blue: #2f8ff0;
    --ink-dark: #1c1c1f;
    --ink-light: #ffffff;
    --outline: #c8cbd0;
  }
  html, body {
    margin: 0;
    width: 772px;
    height: 1200px;
    overflow: hidden;
    background: var(--page);
  }
  .concept-sheet { width: 772px; height: 1200px; display: flex; flex-direction: column; }
  .van-side { display: block; width: 772px; height: 400px; }
  .defs-holder { position: absolute; width: 0; height: 0; }

  .body-outline { fill: none; stroke: var(--outline); stroke-width: 3; }
  .wrap-white { fill: var(--wrap-white); }
  .wrap-black { fill: var(--wrap-black); }
  .side-window { fill: var(--glass); }
  .door-seam { stroke: #9aa0a8; stroke-width: 2; fill: none; }
  .tyre { fill: var(--tyre); }
  .hub { fill: var(--hub); }
  .hub-centre { fill: #8d9096; }

  .swoosh-orange { fill: none; stroke: var(--flame-orange); stroke-linecap: round; }
  .swoosh-amber { fill: none; stroke: var(--flame-amber); stroke-linecap: round; }
  .swoosh-yellow { fill: none; stroke: var(--flame-yellow); stroke-linecap: round; }

  .contact-line {
    font-family: "Rubik", sans-serif;
    font-weight: 700;
    font-size: 40px;
    fill: var(--ink-dark);
  }
  .brand-name {
    font-family: "Rubik", sans-serif;
    font-weight: 800;
    font-size: 92px;
    fill: var(--flame-amber);
    text-anchor: middle;
  }
  .brand-mark { fill: var(--ice-blue); }
  .brand-tagline {
    font-family: "Rubik", sans-serif;
    font-weight: 500;
    font-size: 17px;
    letter-spacing: 3px;
    fill: var(--ink-light);
    text-anchor: middle;
  }
  .service-item {
    font-family: "Rubik", sans-serif;
    font-weight: 700;
    font-size: 32px;
  }
  .service-item.on-dark { fill: var(--ink-light); }
  .service-item.on-light { fill: var(--ink-dark); font-size: 28px; }
  .service-bullet { fill: var(--flame-amber); }

  .badge-ring { fill: var(--wrap-black); stroke: var(--ink-light); stroke-width: 4; }
  .badge-hours {
    font-family: "Rubik", sans-serif; font-weight: 800; font-size: 40px;
    fill: var(--ink-light); text-anchor: middle;
  }
  .badge-word {
    font-family: "Rubik", sans-serif; font-weight: 700; font-size: 15px;
    fill: var(--ink-light); text-anchor: middle;
  }
  .badge-arc {
    font-family: "Rubik", sans-serif; font-weight: 700; font-size: 11px;
    letter-spacing: 1.5px; fill: var(--ink-light);
  }
</style>
</head>
<body>
<svg class="defs-holder" aria-hidden="true">
  <defs>
    <path id="van-body-shape" d="M25,600 L20,455 Q25,380 70,355 L240,300 L470,112 Q500,100 560,100 L1465,104 Q1500,110 1508,200 L1512,600 L1370,615 A125,125 0 0 0 1120,615 L390,615 A130,130 0 0 0 135,612 Z"/>
    <clipPath id="van-body-clip"><use href="#van-body-shape"/></clipPath>
    <path id="badge-top-arc" d="M-38,0 A38,38 0 0 1 38,0"/>
    <path id="badge-bottom-arc" d="M-40,4 A40,40 0 0 0 40,4"/>
  </defs>
</svg>

<main class="concept-sheet">

  <!-- Concept A: diagonal sweep -->
  <svg class="van-side" viewBox="0 0 1540 800" role="img" aria-label="Van side wrap, concept A">
    <g clip-path="url(#van-body-clip)">
      <rect class="wrap-white" x="0" y="0" width="1540" height="800"/>
      <path class="wrap-black" d="M1070,95 C900,120 810,260 730,400 C660,520 570,600 430,612 L1540,612 L1540,95 Z"/>
      <path class="swoosh-orange" stroke-width="40" d="M985,95 C840,170 775,320 700,430 C620,545 530,598 420,608"/>
      <path class="swoosh-amber" stroke-width="22" d="M940,92 C800,170 740,320 668,425 C590,540 505,595 415,606"/>
      <path class="swoosh-yellow" stroke-width="22" d="M905,92 C770,170 712,318 640,420 C565,530 485,590 410,604"/>
    </g>
    <path class="side-window" d="M300,280 L335,140 L640,132 L630,322 L345,330 Z"/>
    <path class="door-seam" d="M685,115 L685,600"/>
    <use class="body-outline" href="#van-body-shape"/>
    <circle class="tyre" cx="262" cy="632" r="108"/><circle class="hub" cx="262" cy="632" r="72"/><circle class="hub-centre" cx="262" cy="632" r="14"/>
    <circle class="tyre" cx="1245" cy="636" r="108"/><circle class="hub" cx="1245" cy="636" r="72"/><circle class="hub-centre" cx="1245" cy="636" r="14"/>

    <text class="contact-line" x="318" y="412">(555) 210-4417</text>
    <text class="contact-line" x="318" y="455">keltrixco.com</text>

    <circle class="brand-mark" cx="1185" cy="215" r="42"/>
    <text class="brand-name" x="1185" y="352">KELTRIX</text>
    <text class="brand-tagline" x="1185" y="385">ELECTRICAL &amp; AIR CONDITIONING</text>

    <g class="service-list">
      <circle class="service-bullet" cx="802" cy="441" r="8"/><text class="service-item on-dark" x="822" y="452">Electrical</text>
      <circle class="service-bullet" cx="802" cy="483" r="8"/><text class="service-item on-dark" x="822" y="494">Air Conditioning</text>
      <circle class="service-bullet" cx="802" cy="525" r="8"/><text class="service-item on-dark" x="822" y="536">Refrigeration &amp;</text>
      <circle class="service-bullet" cx="802" cy="567" r="8"/><text class="service-item on-dark" x="822" y="578">Data</text>
    </g>

    <g class="emergency-badge" transform="translate(1413,493)">
      <circle class="badge-ring" r="50"/>
      <text class="badge-arc"><textPath href="#badge-top-arc" startOffset="50%" text-anchor="middle">EMERGENCY</textPath></text>
      <text class="badge-hours" y="8">24</text>
      <text class="badge-word" y="25">HOUR</text>
      <text class="badge-arc"><textPath href="#badge-bottom-arc" startOffset="50%" text-anchor="middle" dy="12">SERVICE</textPath></text>
    </g>
  </svg>

  <!-- Concept B: white services panel -->
  <svg class="van-side" viewBox="0 0 1540 800" role="img" aria-label="Van side wrap, concept B">
    <g clip-path="url(#van-body-clip)">
      <rect class="wrap-white" x="0" y="0" width="1540" height="800"/>
      <path class="wrap-black" d="M655,95 C710,290 860,370 965,455 C1040,520 1055,580 1050,640 L1540,640 L1540,95 Z"/>
      <path class="swoosh-orange" stroke-width="40" d="M640,100 C690,290 850,375 955,460 C1025,525 1040,590 1035,640"/>
      <path class="swoosh-amber" stroke-width="20" d="M660,120 C710,290 860,370 960,455 C1030,520 1045,590 1040,640"/>
      <path class="swoosh-yellow" stroke-width="20" d="M620,120 C670,300 825,385 930,468 C995,530 1010,590 1005,640"/>
    </g>
    <path class="side-window" d="M300,280 L335,140 L640,132 L630,322 L345,330 Z"/>
    <path class="door-seam" d="M685,115 L685,600"/>
    <use class="body-outline" href="#van-body-shape"/>
    <circle class="tyre" cx="262" cy="632" r="108"/><circle class="hub" cx="262" cy="632" r="72"/><circle class="hub-centre" cx="262" cy="632" r="14"/>
    <circle class="tyre" cx="1245" cy="636" r="108"/><circle class="hub" cx="1245" cy="636" r="72"/><circle class="hub-centre" cx="1245" cy="636" r="14"/>

    <text class="contact-line" x="320" y="458">(555) 210-4417</text>
    <text class="contact-line" x="320" y="500">keltrixco.com</text>

    <circle class="brand-mark" cx="1215" cy="260" r="42"/>
    <text class="brand-name" x="1215" y="398">KELTRIX</text>
    <text class="brand-tagline" x="1215" y="430">ELECTRICAL &amp; AIR CONDITIONING</text>

    <g class="service-list">
      <circle class="service-bullet" cx="709" cy="504" r="7"/><text class="service-item on-light" x="726" y="514">Electrical</text>
      <circle class="service-bullet" cx="709" cy="537" r="7"/><text class="service-item on-light" x="726" y="547">Air Conditioning</text>
      <circle class="service-bullet" cx="709" cy="570" r="7"/><text class="service-item on-light" x="726" y="580">Refrigeration &amp;</text>
      <circle class="service-bullet" cx="709" cy="603" r="7"/><text class="service-item on-light" x="726" y="613">Data</text>
    </g>

    <g class="emergency-badge" transform="translate(835,251) scale(1.1)">
      <circle class="badge-ring" r="50"/>
      <text class="badge-arc"><textPath href="#badge-top-arc" startOffset="50%" text-anchor="middle">EMERGENCY</textPath></text>
      <text class="badge-hours" y="8">24</text>
      <text class="badge-word" y="25">HOUR</text>
      <text class="badge-arc"><textPath href="#badge-bottom-arc" startOffset="50%" text-anchor="middle" dy="12">SERVICE</textPath></text>
    </g>
  </svg>

  <!-- Concept C: vertical flame divider -->
  <svg class="van-side" viewBox="0 0 1540 800" role="img" aria-label="Van side wrap, concept C">
    <g clip-path="url(#van-body-clip)">
      <rect class="wrap-white" x="0" y="0" width="1540" height="800"/>
      <path class="wrap-black" d="M835,95 C795,250 805,400 795,500 C787,570 780,600 770,615 L1540,615 L1540,95 Z"/>
      <path class="swoosh-orange" stroke-width="36" d="M812,95 C765,250 782,420 772,520 C766,570 760,600 748,615"/>
      <path class="swoosh-amber" stroke-width="20" d="M795,110 C755,260 768,420 758,520 C752,570 748,600 738,615"/>
      <path class="swoosh-yellow" stroke-width="16" d="M785,130 C750,270 758,420 748,520"/>
    </g>
    <path class="side-window" d="M300,280 L335,140 L640,132 L630,322 L345,330 Z"/>
    <path class="door-seam" d="M685,115 L685,600"/>
    <use class="body-outline" href="#van-body-shape"/>
    <circle class="tyre" cx="262" cy="632" r="108"/><circle class="hub" cx="262" cy="632" r="72"/><circle class="hub-centre" cx="262" cy="632" r="14"/>
    <circle class="tyre" cx="1245" cy="636" r="108"/><circle class="hub" cx="1245" cy="636" r="72"/><circle class="hub-centre" cx="1245" cy="636" r="14"/>

    <text class="contact-line" x="326" y="400">(555) 210-4417</text>
    <text class="contact-line" x="326" y="442">keltrixco.com</text>

    <circle class="brand-mark" cx="1175" cy="195" r="42"/>
    <text class="brand-name" x="1175" y="330">KELTRIX</text>
    <text class="brand-tagline" x="1175" y="362">ELECTRICAL &amp; AIR CONDITIONING</text>

    <g class="service-list">
      <circle class="service-bullet" cx="862" cy="430" r="7"/><text class="service-item on-dark" x="880" y="440" font-size="28">Electrical</text>
      <circle class="service-bullet" cx="862" cy="465" r="7"/><text class="service-item on-dark" x="880" y="475" font-size="28">Air Conditioning</text>
      <circle class="service-bullet" cx="862" cy="500" r="7"/><text class="service-item on-dark" x="880" y="510" font-size="28">Refrigeration &amp;</text>
      <circle class="service-bullet" cx="862" cy="535" r="7"/><text class="service-item on-dark" x="880" y="545" font-size="28">Data</text>
    </g>

    <g class="emergency-badge" transform="translate(1397,442)">
      <circle class="badge-ring" r="50"/>
      <text class="badge-arc"><textPath href="#badge-top-arc" startOffset="50%" text-anchor="middle">EMERGENCY</textPath></text>
      <text class="badge-hours" y="8">24</text>
      <text class="badge-word" y="25">HOUR</text>
      <text class="badge-arc"><textPath href="#badge-bottom-arc" startOffset="50%" text-anchor="middle" dy="12">SERVICE</textPath></text>
    </g>
  </svg>

</main>
</body>
</html>
```